Need updated stationery design for chiropractic clinic

We recently moved our office and are looking to refresh our letterhead, business cards, presentation folder and envelopes. I tend to prefer simple, clean designs. We communicate with a lot of attorneys and want to exude professionalism. I have attached our logo and 2 additional versions (all white and white letters instead of grey).

Target Market(s)

Other medical professionals and attorneys. Business cards will go to patients as well.

Industry/Entity Type

Healthcare

```html
<!DOCTYPE html>
<html lang="en">
<head>
<meta charset="utf-8">
<title>Keystone Spine Stationery</title>
<link href="https://fonts.googleapis.com/css2?family=Montserrat:wght@400;500;600;700&display=swap" rel="stylesheet">
<style>
  :root {
    --blue: #0a98d2;
    --teal: #00c8d1;
    --ink: #2b2b2b;
    --muted: #555a60;
    --paper: #ffffff;
    --stage: #e7e9ec;
    --faint: #eeeff1;
    --envelope: #e9eaec;
  }
  * { box-sizing: border-box; margin: 0; padding: 0; }
  html, body { width: 1028px; height: 1200px; overflow: hidden; }
  body {
    background: var(--stage);
    font-family: "Montserrat", Arial, sans-serif;
    color: var(--ink);
    position: relative;
  }
  .sheet {
    position: absolute;
    background: var(--paper);
    box-shadow: 0 2px 8px rgba(0,0,0,.12);
    overflow: hidden;
  }
  .wordmark {
    display: flex; align-items: center; gap: 7px;
    color: var(--blue); font-weight: 700; white-space: nowrap;
  }
  .wordmark .mark-square { background: var(--blue); display: block; }

  /* Letterhead */
  .letterhead { left: 40px; top: 40px; width: 460px; height: 650px; padding: 30px 30px; }
  .letterhead .wordmark { font-size: 18px; }
  .letterhead .mark-square { width: 16px; height: 16px; }
  .sender { margin-top: 62px; }
  .sender-name { color: var(--blue); font-weight: 700; font-size: 14px; letter-spacing: .3px; }
  .sender-line { font-size: 8.5px; color: var(--muted); margin-top: 5px; line-height: 1.3; }
  .letter-date { position: absolute; right: 30px; top: 206px; font-size: 9px; font-weight: 500; }
  .letter-body { margin-top: 28px; font-size: 7.2px; line-height: 1.42; text-align: justify; color: #333; }
  .letter-body p { margin-bottom: 10px; }
  .closing { margin-top: 18px; font-size: 11px; color: #444; }
  .signature-area { margin-top: 10px; width: 90px; height: 46px; background: var(--faint); }
  .contact-list { position: absolute; left: 30px; bottom: 28px; font-size: 8.5px; color: #333; }
  .contact-list li { list-style: none; display: flex; align-items: center; gap: 6px; margin-top: 5px; }
  .contact-icon { width: 10px; height: 10px; background: var(--teal); border-radius: 2px; display: inline-flex; align-items: center; justify-content: center; }
  .faint-decoration { position: absolute; right: 0; bottom: 0; width: 170px; height: 170px;
    background: linear-gradient(135deg, #f6f6f7 0%, #e9eaec 100%); }

  /* Folder */
  .folder { left: 528px; top: 40px; width: 460px; height: 650px; }
  .folder .wordmark { position: absolute; right: 30px; top: 40px; font-size: 24px; }
  .folder .mark-square { width: 22px; height: 22px; }
  .folder-art { position: absolute; left: 20px; right: 0; top: 205px; bottom: 0;
    background: linear-gradient(135deg, var(--teal) 0%, var(--blue) 55%, var(--teal) 100%); }
  .folder-url { position: absolute; left: 20px; bottom: 22px; font-size: 16px; color: var(--blue); font-weight: 500;
    background: var(--paper); padding: 4px 8px 4px 0; }

  /* Business cards */
  .card { width: 300px; height: 172px; left: 40px; }
  .card-back { top: 720px; padding: 18px 18px; }
  .card-back .wordmark { font-size: 12px; }
  .card-back .mark-square { width: 10px; height: 10px; }
  .card-person { position: absolute; right: 18px; top: 20px; text-align: right; }
  .card-person .name { color: var(--blue); font-weight: 700; font-size: 11px; }
  .card-person .role { font-size: 7px; color: var(--muted); margin-top: 2px; }
  .card-back .contact-list { left: 18px; bottom: 16px; font-size: 6.5px; }
  .card-back .contact-icon { width: 7px; height: 7px; }
  .card-back .faint-decoration { width: 95px; height: 110px; }
  .card-front { top: 912px; }
  .card-front .card-art { position: absolute; left: 0; top: 0; width: 170px; height: 172px;
    background: linear-gradient(135deg, var(--teal) 0%, var(--blue) 60%, var(--teal) 100%); }
  .card-front .wordmark { position: absolute; right: 16px; bottom: 34px; font-size: 15px; }
  .card-front .mark-square { width: 12px; height: 12px; }

  /* Envelope */
  .envelope { left: 360px; top: 740px; width: 628px; height: 276px; background: var(--envelope); }
  .envelope-flap { position: absolute; left: 0; top: 0; width: 100%; height: 78px; }
  .envelope .wordmark { position: absolute; left: 50%; top: 20px; transform: translateX(-50%); font-size: 20px; }
  .envelope .mark-square { width: 17px; height: 17px; }
  .return-address { position: absolute; left: 26px; bottom: 24px; font-size: 7.5px; color: var(--muted); line-height: 1.4; }
  .envelope .faint-decoration { width: 160px; height: 150px; background: linear-gradient(135deg, #dcdde0, #d3d5d8); }
</style>
</head>
<body>

<section class="sheet letterhead">
  <div class="wordmark"><span class="mark-square"></span>Keystone Spine</div>
  <div class="sender">
    <div class="sender-name">DANA WHITFIELD</div>
    <div class="sender-line">0155-204-318</div>
    <div class="sender-line">hello@keystonespine.com</div>
    <div class="sender-line">418 Meridian Ave. Suite<br>210 Plano, TX 75000</div>
  </div>
  <div class="letter-date">12 December, 2023</div>
  <div class="letter-body">
    <p>Lorem ipsum dolor sit amet, consectetuer adipiscing elit, sed diam nonummy nibh euismod tincidunt ut laoreet dolore magna aliquam erat volutpat. Ut wisi enim ad minim veniam, quis nostrud exerci tation ullamcorper suscipit lobortis nisl ut aliquip ex ea commodo consequat. Duis autem vel eum iriure dolor in hendrerit in vulputate velit esse molestie consequat, vel illum dolore eu feugiat nulla facilisis at vero eros et accumsan et iusto odio dignissim qui blandit praesent luptatum zzril delenit augue duis dolore te feugait nulla facilisi.</p>
    <p>Lorem ipsum dolor sit amet, cons ectetuer adipiscing elit, sed diam nonummy nibh euismod tincidunt ut laoreet dolore magna aliquam erat volutpat. Ut wisi enim ad minim veniam, quis nostrud exerci tation ullamcorper suscipit lobortis nisl ut aliquip ex ea commodo consequat.<br>Lorem ipsum dolor sit amet, consectetuer adipiscing elit, sed diam nonummy nibh euismod tincidunt ut laoreet dolore magna aliquam erat</p>
    <p>Lorem ipsum dolor sit amet, cons ectetuer adipiscing elit, sed diam nonummy nibh euismod tincidunt ut laoreet dolore magna aliquam erat volutpat. Ut wisi enim ad minim veniam, quis nostrud exerci tation ullamcorper suscipit lobortis nisl ut aliquip ex ea commodo consequat. Lorem ipsum dolor sit amet, consectetuer adipiscing elit, sed diam nonummy nibh euismod tincidunt ut laoreet dolore magna aliquam erat volutpat. Ut wisi enim ad minim veniam, quis nostrud exerci tation ullamcorper suscipit lobortis nisl ut aliquip ex ea commodo consequat. Duis autem vel eum iriure.</p>
  </div>
  <div class="closing">Managing Director</div>
  <div class="signature-area" role="img" aria-label="Handwritten signature"></div>
  <ul class="contact-list">
    <li><span class="contact-icon"><svg width="6" height="6" viewBox="0 0 10 10"><path d="M2 1l2 2-1 1.5c.8 1.5 1.5 2.2 3 3L7.5 6l2 2-1.5 1.5C4.5 9 1 5.5.5 2.5z" fill="#fff"/></svg></span>0155-204-318</li>
    <li><span class="contact-icon"><svg width="6" height="6" viewBox="0 0 10 10"><rect x="0.5" y="2" width="9" height="6" fill="none" stroke="#fff"/><path d="M.5 2L5 5.5 9.5 2" fill="none" stroke="#fff"/></svg></span>hello@keystonespine.com</li>
    <li><span class="contact-icon"><svg width="6" height="6" viewBox="0 0 10 10"><path d="M2 1l6 4-3 .6L6.8 9 5.6 9.5 4 6.3 2 8z" fill="#fff"/></svg></span>www.keystonespine.com</li>
  </ul>
  <div class="faint-decoration" role="img" aria-label="Faint brand decoration"></div>
</section>

<section class="sheet folder">
  <div class="wordmark"><span class="mark-square"></span>Keystone Spine</div>
  <div class="folder-art" role="img" aria-label="Large brand decoration in blue and teal"></div>
  <div class="folder-url">www.keystonespine.com</div>
</section>

<section class="sheet card card-back">
  <div class="wordmark"><span class="mark-square"></span>Keystone Spine</div>
  <div class="card-person">
    <div class="name">DANA WHITFIELD</div>
    <div class="role">Manager</div>
  </div>
  <ul class="contact-list">
    <li><span class="contact-icon"></span>0155-204-318</li>
    <li><span class="contact-icon"></span>hello@keystonespine.com</li>
    <li><span class="contact-icon"></span>www.keystonespine.com</li>
  </ul>
  <div class="faint-decoration" role="img" aria-label="Faint brand decoration"></div>
</section>

<section class="sheet card card-front">
  <div class="card-art" role="img" aria-label="Brand decoration in blue and teal"></div>
  <div class="wordmark"><span class="mark-square"></span>Keystone Spine</div>
</section>

<section class="sheet envelope">
  <svg class="envelope-flap" viewBox="0 0 628 78" preserveAspectRatio="none" aria-hidden="true">
    <path d="M0 0H628L612 62Q608 78 590 78H38Q20 78 16 62Z" fill="#ffffff"/>
  </svg>
  <div class="wordmark"><span class="mark-square"></span>Keystone Spine</div>
  <div class="return-address">418 Meridian Ave. Suite<br>210 Plano, TX 75000</div>
  <div class="faint-decoration" role="img" aria-label="Faint brand decoration"></div>
</section>

</body>
</html>
```